Haskell and Dunmore Ranch Insurance

Would like you all to design a logo for our Business cards and possible letterhead.
This business provides Ranch insurance for folks in Texas, New Mexico, and Oklahoma

Ggood stuff everybody, be sure to include email and Mobil for both of us on all designs

Thanks

Hello All

Wanted to let you all know i am going to extend deadline a few days, and add some more $$ to the budget

Reason: Give everybody a bit ,more time, and I added more money

Appreciate all of yalls hard work, will review and provide feed back hopefully today, been a little whacky with the holidays and all

```html
<!DOCTYPE html>
<html lang="en">
<head>
<meta charset="utf-8">
<title>Haskell and Dunmore Ranch Insurance – Business Card</title>
<link rel="stylesheet" href="https://fonts.googleapis.com/css2?family=Questrial&display=swap">
<style>
  :root {
    --page: #f1f1f1;
    --card-dark: #1c1c1e;
    --card-mid: #2b2b2e;
    --accent-red: #d8222b;
    --text-light: #f4f4f4;
    --silver-light: #e9e9ea;
    --silver-dark: #8d8e91;
  }
  * { margin: 0; padding: 0; box-sizing: border-box; }
  html, body {
    width: 1200px;
    height: 900px;
    overflow: hidden;
    background: var(--page);
    font-family: "Questrial", sans-serif;
  }
  .business-card {
    position: absolute;
    left: 100px;
    top: 164px;
    width: 1000px;
    height: 572px;
    border-radius: 44px;
    overflow: hidden;
    box-shadow: 0 18px 40px rgba(0,0,0,0.28);
  }
  .card-texture {
    position: absolute;
    inset: 0;
    background: radial-gradient(ellipse at 40% 45%, var(--card-mid) 0%, var(--card-dark) 75%);
  }
  .divider {
    position: absolute;
    top: 0;
    bottom: 0;
    left: 548px;
    width: 8px;
    background: linear-gradient(180deg, var(--silver-dark) 0%, var(--silver-light) 30%, #ffffff 50%, var(--silver-light) 70%, var(--silver-dark) 100%);
    box-shadow: 0 0 14px rgba(255,255,255,0.35);
  }
  .brand {
    position: absolute;
    left: 0;
    width: 548px;
    top: 0;
    bottom: 0;
    display: flex;
    align-items: center;
    justify-content: center;
    gap: 18px;
  }
  .brand-square {
    width: 30px;
    height: 30px;
    background: var(--accent-red);
    flex: none;
  }
  .brand-name {
    color: var(--silver-light);
    font-size: 40px;
    letter-spacing: 1px;
    white-space: nowrap;
  }
  .contacts {
    position: absolute;
    left: 584px;
    top: 68px;
    color: var(--text-light);
    font-size: 24px;
    line-height: 34px;
  }
  .contact-block { margin-bottom: 44px; }
  .contact-block.office { margin-top: 40px; }
  .person-name {
    color: var(--accent-red);
    font-size: 28px;
    line-height: 40px;
    padding-left: 34px;
  }
  .contact-line {
    display: flex;
    align-items: center;
    gap: 8px;
    white-space: nowrap;
  }
  .contact-line.indent { padding-left: 34px; }
  .icon { width: 24px; height: 24px; flex: none; fill: var(--accent-red); }
</style>
</head>
<body>
  <div class="business-card">
    <div class="card-texture" role="img" aria-label="Dark perforated carbon texture"></div>
    <div class="divider"></div>

    <div class="brand">
      <span class="brand-square"></span>
      <span class="brand-name">Haskell and Dunmore</span>
    </div>

    <div class="contacts">
      <div class="contact-block">
        <div class="person-name">Ty Dunmore</div>
        <div class="contact-line">
          <svg class="icon" viewBox="0 0 24 24"><path d="M2 5h20v14H2z M3.5 6.5 12 13l8.5-6.5" fill="none" stroke="#d8222b" stroke-width="2.2"/></svg>
          <span>ty@haskellanddunmore.com</span>
        </div>
        <div class="contact-line">
          <svg class="icon" viewBox="0 0 24 24"><path d="M6 1h12v22H6z M8 3v14h8V3z M11 19h2v2h-2z"/></svg>
          <span>cell # 325-555-0148</span>
        </div>
      </div>

      <div class="contact-block">
        <div class="person-name">Roy Haskell</div>
        <div class="contact-line">
          <svg class="icon" viewBox="0 0 24 24"><path d="M2 5h20v14H2z M3.5 6.5 12 13l8.5-6.5" fill="none" stroke="#d8222b" stroke-width="2.2"/></svg>
          <span>haskellr@hdranchco.com</span>
        </div>
        <div class="contact-line">
          <svg class="icon" viewBox="0 0 24 24"><path d="M6 1h12v22H6z M8 3v14h8V3z M11 19h2v2h-2z"/></svg>
          <span>cell # 512-555-0177</span>
        </div>
      </div>

      <div class="contact-block office">
        <div class="contact-line">
          <svg class="icon" viewBox="0 0 24 24"><path d="M6.6 10.8a15.1 15.1 0 0 0 6.6 6.6l2.2-2.2a1 1 0 0 1 1-.25 11.4 11.4 0 0 0 3.6.57 1 1 0 0 1 1 1V20a1 1 0 0 1-1 1A17 17 0 0 1 3 4a1 1 0 0 1 1-1h3.5a1 1 0 0 1 1 1c0 1.25.2 2.450.57 3.57a1 1 0 0 1-.25 1z"/></svg>
          <span>325.555.0190</span>
        </div>
        <div class="contact-line">
          <svg class="icon" viewBox="0 0 24 24"><path d="M12 3 2 12h3v9h5v-6h4v6h5v-9h3z"/></svg>
          <span>408 W Oak St.</span>
        </div>
        <div class="contact-line indent">
          <span>Cedar Flats, TX 76911</span>
        </div>
        <div class="contact-line">
          <svg class="icon" viewBox="0 0 24 24"><g fill="none" stroke="#d8222b" stroke-width="2"><circle cx="12" cy="12" r="10"/><ellipse cx="12" cy="12" rx="4.5" ry="10"/><path d="M2 12h20M4 7h16M4 17h16"/></g></svg>
          <span>www.haskellanddunmore.com</span>
        </div>
      </div>
    </div>
  </div>
</body>
</html>
```